Health care technology software systems

We have a solid logo. We have company colors that will need to be used as well. We just need a great business card design. We sell to health plans but want to be modern

Target Market(s)

Health technology sector selling into Health Plans

Industry/Entity Type

Health Care Technology

Contact Information for Business Card

Name, title, address, phone number, email

Requirements
Must have
• Use of Parvexa corporate colors - Uploaded w/ our logos

```html
<!DOCTYPE html>
<html lang="en">
<head>
<meta charset="utf-8">
<title>Parvexa Business Card</title>
<link rel="stylesheet" href="https://fonts.googleapis.com/css2?family=Quicksand:wght@400;500&family=Lato:wght@400;700&display=swap">
<style>
  :root {
    --bg: #1b1c1c;
    --card-dark: #363836;
    --card-light: #ffffff;
    --ink: #2f302f;
    --green: #7fc31c;
    --blue: #3a5bb5;
    --sky: #1aa4de;
    --band-text: #ffffff;
  }
  * { margin: 0; padding: 0; box-sizing: border-box; }
  html, body { width: 1200px; height: 1015px; overflow: hidden; background: var(--bg); }
  .canvas {
    width: 1200px; height: 1015px;
    display: flex; flex-direction: column; align-items: center; justify-content: center; gap: 60px;
  }
  .card { width: 700px; height: 400px; position: relative; overflow: hidden; box-shadow: 0 12px 30px rgba(0,0,0,.5); }

  /* Back */
  .card--back { background: var(--card-dark); display: flex; align-items: center; justify-content: center; }
  .brand { display: flex; align-items: center; gap: 22px; }
  .brand__dot { width: 58px; height: 58px; border-radius: 50%; background: var(--sky); }
  .brand__name { font-family: "Quicksand", sans-serif; font-weight: 400; font-size: 72px; letter-spacing: 1px; line-height: 1; }
  .card--back .brand__name { color: #ffffff; }

  /* Front */
  .card--front { background: var(--card-light); }
  .card--front .brand { position: absolute; top: 88px; left: 330px; gap: 18px; }
  .card--front .brand__dot { width: 48px; height: 48px; }
  .card--front .brand__name { color: var(--ink); font-size: 60px; }
  .accent { position: absolute; left: 0; top: 126px; width: 20px; height: 30px; background: var(--green); }
  .person { position: absolute; left: 62px; top: 98px; }
  .person__name { font-family: "Quicksand", sans-serif; font-weight: 400; font-size: 36px; color: var(--ink); line-height: 1; }
  .person__title { font-family: "Lato", sans-serif; font-weight: 700; font-size: 18px; color: var(--ink); margin-top: 6px; letter-spacing: .3px; }

  .band { position: absolute; left: 0; top: 252px; width: 100%; height: 66px; background: var(--card-dark); }
  .contact { position: absolute; top: 0; font-family: "Lato", sans-serif; font-size: 17px; color: var(--band-text); letter-spacing: .3px; }
  .contact__icon {
    position: absolute; top: -20px; width: 40px; height: 40px; border-radius: 50%;
    border: 3px solid #ffffff; display: flex; align-items: center; justify-content: center;
  }
  .contact__text { position: absolute; top: 28px; white-space: nowrap; }
  .contact--email .contact__icon { left: 56px; background: var(--blue); }
  .contact--email .contact__text { left: 40px; }
  .contact--phone .contact__icon { left: 330px; background: var(--green); }
  .contact--phone .contact__text { left: 290px; }
  .contact--web .contact__icon { left: 556px; background: var(--sky); }
  .contact--web .contact__text { left: 470px; }
  .address { position: absolute; top: 342px; left: 0; width: 100%; text-align: center; font-family: "Lato", sans-serif; font-size: 18px; color: var(--ink); letter-spacing: .3px; }
</style>
</head>
<body>
<main class="canvas">
  <section class="card card--back">
    <div class="brand">
      <span class="brand__dot"></span>
      <span class="brand__name">parvexa</span>
    </div>
  </section>

  <section class="card card--front">
    <div class="accent"></div>
    <div class="person">
      <p class="person__name">Daniel Harper</p>
      <p class="person__title">Managing Director</p>
    </div>
    <div class="brand">
      <span class="brand__dot"></span>
      <span class="brand__name">parvexa</span>
    </div>

    <div class="band">
      <div class="contact contact--email">
        <span class="contact__icon">
          <svg width="20" height="14" viewBox="0 0 20 14" aria-hidden="true"><rect x="1" y="1" width="18" height="12" fill="#fff"/><path d="M1 1 L10 8 L19 1" fill="none" stroke="#3a5bb5" stroke-width="1.5"/></svg>
        </span>
        <span class="contact__text">hello@parvexa-health.com</span>
      </div>
      <div class="contact contact--phone">
        <span class="contact__icon">
          <svg width="18" height="18" viewBox="0 0 24 24" aria-hidden="true"><path fill="#fff" d="M6.6 10.8a15 15 0 0 0 6.6 6.6l2.2-2.2c.3-.3.7-.4 1-.2 1.1.4 2.3.6 3.6.6.6 0 1 .4 1 1V20c0 .6-.4 1-1 1A17 17 0 0 1 3 4c0-.6.4-1 1-1h3.5c.6 0 1 .4 1 1 0 1.3.2 2.5.6 3.6.1.3 0 .7-.2 1z"/></svg>
        </span>
        <span class="contact__text">044-555 018 342</span>
      </div>
      <div class="contact contact--web">
        <span class="contact__icon">
          <svg width="20" height="20" viewBox="0 0 20 20" aria-hidden="true" fill="none" stroke="#fff" stroke-width="1.4"><circle cx="10" cy="10" r="8"/><ellipse cx="10" cy="10" rx="3.5" ry="8"/><path d="M2 10h16M3.5 6h13M3.5 14h13"/></svg>
        </span>
        <span class="contact__text">www.parvexa-health.com</span>
      </div>
    </div>

    <p class="address">88, Meridian Way Harborview, 30417</p>
  </section>
</main>
</body>
</html>
```